Ferris + Oakdale Architecture Ltd Stationary rebrand Lead designer to create a fresh clean modern...

We have recieved a great new logo design and now we are after a consistant fresh and modern stationary to match the new design. Business card design, Letter Head design, presentatnion folders and other stationery within the package. I have also added some of our existing layouts for presentation we would like updating with the new look, We would like a clean modern fresh design that looks visually pleasing on the page. we cant wait to see what you come up with!!!!

Target Market(s)

young professionals and middle age clients

Industry/Entity Type

Architect

Contact Information for Business Card

i have uploarded our orginal business card that has all the details attached.

Font styles to use
Sans Serif

Colors
000000
ffffff
d3d3d3

Requirements
Must have
• Logo and our contact information
Nice to have
• white sape around the card to give a clean look.

```html
<!DOCTYPE html>
<html lang="en">
<head>
<meta charset="utf-8">
<title>Ferris + Oakdale Architecture Ltd — Letterhead</title>
<link rel="stylesheet" href="https://fonts.googleapis.com/css2?family=Roboto+Condensed:wght@300;400&family=Cinzel:wght@500&family=Open+Sans:wght@400;700&display=swap">
<style>
  :root {
    --backdrop: #d3d3d3;
    --paper: #ffffff;
    --ink: #1e1e1e;
    --body-grey: #8a8a8a;
    --muted: #7a7a7a;
    --accent: #8dc63f;
    --rule: #9a9a9a;
  }
  * { box-sizing: border-box; margin: 0; padding: 0; }
  html, body { width: 1200px; height: 1200px; overflow: hidden; background: var(--backdrop); }
  .letterhead {
    position: absolute; left: 175px; top: 0;
    width: 850px; height: 1200px;
    background: var(--paper);
    border-top: 6px solid var(--ink);
  }
  .brand {
    position: absolute; top: 30px; left: 0; right: 0;
    display: flex; flex-direction: column; align-items: center;
    font-family: "Roboto Condensed", sans-serif; font-weight: 400; color: var(--ink);
  }
  .brand-square { width: 104px; height: 104px; background: var(--ink); margin-bottom: 22px; }
  .brand-name { font-size: 23px; letter-spacing: 4px; line-height: 1; }
  .brand-sub { font-size: 12px; letter-spacing: 14px; margin-top: 8px; margin-right: -14px; }
  .letter-body {
    position: absolute; left: 96px; width: 664px;
    font-family: "Roboto Condensed", sans-serif; font-weight: 300;
    font-size: 17px; line-height: 26.2px; color: var(--body-grey);
  }
  .para-one { top: 257px; }
  .para-two { top: 467px; }
  .para-three { top: 703px; }
  .signature {
    position: absolute; left: 96px; top: 995px; width: 285px; height: 62px;
    background: linear-gradient(90deg, #f2f2f2, #e6e6e6);
  }
  .footer { position: absolute; left: 0; right: 0; top: 1110px; text-align: center; }
  .footer-name {
    font-family: "Cinzel", serif; font-weight: 500; font-size: 17px;
    letter-spacing: 0.5px; color: var(--ink);
  }
  .footer-icons { display: flex; align-items: center; justify-content: center; gap: 22px; margin-top: 8px; }
  .footer-icons .rule { width: 85px; height: 1px; background: var(--rule); }
  .footer-icons svg { width: 17px; height: 17px; display: block; }
  .contact-line {
    margin-top: 13px; font-family: "Open Sans", sans-serif; font-size: 11.2px;
    color: var(--muted); white-space: nowrap;
  }
  .contact-line strong { color: var(--ink); font-weight: 700; }
  .contact-line .sep { color: var(--accent); margin: 0 5px; }
</style>
</head>
<body>
<main class="letterhead">
  <header class="brand">
    <div class="brand-square"></div>
    <div class="brand-name">FERRIS + OAKDALE</div>
    <div class="brand-sub">ARCHITECTURE</div>
  </header>

  <p class="letter-body para-one">Lorem Ipsum is simply dummy text of the printing and typesetting industry. Lorem Ipsum has been the industry’s standard dummy text ever since the 1500s, when an unknown printer took a galley of type and scrambled it to make a type specimen book. It has survived not only five centuries, but also the leap into electronic typesetting, remaining essentially unchanged. It was popularised in the 1960s with the release of Typeline sheets containing Lorem Ipsum passages, and more recently with desktop publishing software like Quillset Layout including versions of Lorem Ipsum.</p>

  <p class="letter-body para-two">It is a long established fact that a reader will be distracted by the readable content of a page when looking at its layout. The point of using Lorem Ipsum is that it has a more-or-less normal distribution of letters, as opposed to using ’Content here, content here’, making it look like readable English. Many desktop publishing packages and web page editors now use Lorem Ipsum as their default model text, and a search for ’lorem ipsum’ will uncover many web sites still in their infancy. Various versions have evolved over the years, sometimes by accident, sometimes on purpose (injected humour and the like).</p>

  <p class="letter-body para-three">Contrary to popular belief, Lorem Ipsum is not simply random text. It has roots in a piece of classical Latin literature from 45 BC, making it over 2000 years old. Edwin Harrow, a Latin professor at Westbrook College in Vermont, looked up one of the more obscure Latin words, consectetur, from a Lorem Ipsum passage, and going through the cites of the word in classical literature, discovered the undoubtable source. Lorem Ipsum comes from sections 1.10.32 and 1.10.33 of "de Finibus Bonorum et Malorum" structures, to generate Lorem Ipsum which looks reasonable. The generated Lorem Ipsum is therefore always free from repetition, injected humour, or non-characteristic words etc.</p>

  <div class="signature" role="img" aria-label="Handwritten signature of the sender"></div>

  <footer class="footer">
    <div class="footer-name">Ferris + Oakdale Architecture Ltd</div>
    <div class="footer-icons">
      <span class="rule"></span>
      <svg viewBox="0 0 20 20" aria-label="Address"><circle cx="10" cy="10" r="10" fill="var(--accent)"/><path d="M10 4.5a3.6 3.6 0 0 0-3.6 3.6c0 2.7 3.6 6.9 3.6 6.9s3.6-4.2 3.6-6.9A3.6 3.6 0 0 0 10 4.5z" fill="#fff"/><circle cx="10" cy="8.1" r="1.4" fill="var(--accent)"/></svg>
      <svg viewBox="0 0 20 20" aria-label="Phone"><circle cx="10" cy="10" r="10" fill="var(--accent)"/><path d="M7 4.8l1.6 2.6-1 1.1c.7 1.6 1.8 2.8 3.4 3.6l1.1-1 2.6 1.6-.8 1.9c-4.2-.3-7.6-3.7-8-8z" fill="#fff"/></svg>
      <svg viewBox="0 0 20 20" aria-label="Email"><circle cx="10" cy="10" r="10" fill="var(--accent)"/><rect x="5" y="6.5" width="10" height="7" rx="1" fill="#fff"/><path d="M5.5 7l4.5 3.5L14.5 7" fill="none" stroke="var(--accent)" stroke-width="1"/></svg>
      <svg viewBox="0 0 20 20" aria-label="Website"><circle cx="10" cy="10" r="10" fill="var(--accent)"/><g fill="none" stroke="#fff" stroke-width="1"><circle cx="10" cy="10" r="5"/><ellipse cx="10" cy="10" rx="2.2" ry="5"/><path d="M5 10h10M6 7.3h8M6 12.7h8"/></g></svg>
      <span class="rule"></span>
    </div>
    <div class="contact-line"><strong>42 Larch Road, Kelmore 7712</strong><span class="sep">|</span><strong>PO Box 3180, Kelmore 7745</strong><span class="sep">|</span>03 555 0184<span class="sep">|</span>hello@foarchitecture.co.nz<span class="sep">|</span>www.foarchitecture.co.nz</div>
  </footer>
</main>
</body>
</html>
```